Camp Thornbrook 2021 Magazine Design

We are for someone to design our annual magazine/newsletter. This is a print newsletter that is a total of 20 pages. It will need to be designed in a way that is easy to share with our printers. The designer will need to be someone who is creative and easy to work with.
For those interested in this project we ask that you design 4 to 6 pages for us to view. Once we select the designer we will want the rest created in a two-week time span. For those submitting a bid please include front cover, theme & dates, mission & vision, and Lend a Hand Forward.

This link will provide the layout of the newsletter https://files.pelmarsh.example/doc/7qTzR2kLpW9xVbN4cHsYd/view.

This link will provide you with the pictures that are needed and a few documents https://files.pelmarsh.example/folder/3hGvK8mQxZ5rLtP1wNcBj/view

Details:
20 pages long (including covers)
8.5 x 11

Please message me if you need any further details.

Target Market(s)

Our alumni base. Covers all ages

Requirements
Must have
• Spelled out in document
Nice to have
• Spelled out in document
Should not have
• Spelled out in document

```html
<!DOCTYPE html>
<html lang="en">
<head>
<meta charset="utf-8">
<title>Camp Thornbrook – Mission / Vision Spread</title>
<link href="https://fonts.googleapis.com/css2?family=Raleway:wght@200;300&family=Open+Sans:wght@400;600;700&display=swap" rel="stylesheet">
<style>
  :root {
    --backdrop: #a4a4a4;
    --paper: #ffffff;
    --ink: #2b2b2b;
    --ember: #e08a4f;
    --ember-soft: #e9a06a;
    --forest: #1f302b;
    --bark: #3b3a2e;
    --sand: #c88c55;
    --white: #ffffff;
  }
  * { box-sizing: border-box; margin: 0; padding: 0; }
  html, body { width: 1200px; height: 900px; overflow: hidden; }
  body {
    background: var(--backdrop);
    font-family: "Open Sans", sans-serif;
    color: var(--ink);
    position: relative;
  }
  .spread {
    position: absolute;
    left: 50px; top: 94px;
    width: 1100px; height: 712px;
    display: flex;
    background: var(--paper);
  }
  .page { position: relative; width: 550px; height: 712px; overflow: hidden; }
  .page--left { border-right: 1px solid #e4e4e4; }

  /* Left page */
  .hero-photo {
    position: absolute; left: 0; top: 0; width: 300px; height: 712px;
    background: linear-gradient(180deg, var(--bark) 0%, #6a5338 45%, var(--sand) 80%, #d3a26c 100%);
  }
  .page-title {
    position: absolute; left: 28px; top: 62px;
    font-family: "Raleway", sans-serif; font-weight: 200;
    font-size: 26px; color: var(--white); letter-spacing: 0.5px;
  }
  .story {
    position: absolute; width: 205px;
    font-size: 8.6px; font-weight: 700; line-height: 1.45;
    color: var(--ink);
  }
  .story--top { left: 322px; top: 30px; }
  .story--bottom { left: 322px; top: 448px; }
  .story--bottom p { text-indent: 80px; }
  .accent-disc {
    position: absolute; left: 236px; top: 298px;
    width: 140px; height: 140px; border-radius: 50%;
    border: 5px solid var(--white);
    background: radial-gradient(circle at 70% 75%, var(--ember-soft) 0%, var(--ember) 35%, #6b4a34 75%, var(--bark) 100%);
  }

  /* Right page */
  .gate-photo {
    position: absolute; left: 18px; top: 18px; width: 514px; height: 318px;
    background: linear-gradient(180deg, #5d4a38 0%, var(--ember) 30%, #b57a4c 60%, #5a4a3a 100%);
  }
  .card { position: absolute; border-radius: 9px; color: var(--white); padding: 16px 18px; }
  .card h2 {
    font-family: "Raleway", sans-serif; font-weight: 300;
    font-size: 19px; margin-bottom: 10px;
  }
  .card--vision { left: 18px; top: 350px; width: 232px; height: 110px; background: var(--ember); }
  .card--vision ul { list-style: none; font-size: 7.5px; line-height: 2; }
  .card--mission { left: 262px; top: 338px; width: 270px; height: 122px; background: var(--forest); }
  .card--mission p { font-size: 7.6px; font-weight: 600; line-height: 1.45; }
  .card--values {
    left: 18px; top: 474px; width: 514px; height: 180px;
    background:
      radial-gradient(ellipse at 55% 10%, rgba(240,150,90,0.9) 0%, rgba(240,150,90,0) 45%),
      linear-gradient(100deg, var(--ember-soft) 0%, var(--ember) 35%, #6a4a36 70%, var(--forest) 100%);
    padding: 22px 22px;
  }
  .card--values ul { list-style: none; font-size: 7.6px; line-height: 1.7; }
</style>
</head>
<body>
  <main class="spread">
    <section class="page page--left">
      <div class="hero-photo" role="img" aria-label="Photo of a weathered wooden cross set on a tree stump in the woods, warm sepia tones"></div>
      <h1 class="page-title">Mission/Vision</h1>

      <div class="story story--top">
        <p>Last year, we were asked by another camp director, “What is your mission statement?” We knew what we did at Camp Thornbrook, but didn’t really know how to efficiently describe what the mission looked like. This led to some self evaluation of our mission, vision, and core values. You may have noticed that we have been putting “Christ - Community - Creation” on everything. It’s on our new logo, it’s on almost all of our social media posts, at the end of our emails, and on all of our materials that we send out through the mail. We decided that these three things were the heart of the Thornbrook experience. This self evaluation led to the creation of our mission statement: “We want to strengthen young people’s relationship with Christ through meaningful worship experiences, create an environment that promotes community through Christ-centered relationships, and provide</p>
      </div>

      <div class="accent-disc" role="img" aria-label="Round tagline badge"></div>

      <div class="story story--bottom">
        <p>opportunities to experience God’s presence through His creation.” Because of our new mission statement, we’ve made “Encountering Christ, Community, and Creation” our vision statement and tagline in hopes to help continue to promote a culture that we have all experienced and grown to love and know during our time together at Thornbrook. Our hope is that through the direction and guidance of our mission, vision, and core value statements, we will continue to carry on the legacy of mission that so many have experienced on the grounds at camp.</p>
      </div>
    </section>

    <section class="page page--right">
      <div class="gate-photo" role="img" aria-label="Photo of two children seen from behind, arm in arm, looking through the camp entrance gate"></div>

      <article class="card card--vision">
        <h2>Our Vision</h2>
        <ul>
          <li>• Encountering Christ</li>
          <li>• Encountering Community</li>
          <li>• Encountering Creation</li>
        </ul>
      </article>

      <article class="card card--mission">
        <h2>Our Mission</h2>
        <p>We want to strengthen young people’s relationship with Christ through meaningful worship experiences, create an environment that promotes community through Christ-centered relationships, and provide opportunities to experience God’s presence through His creation.</p>
      </article>

      <article class="card card--values">
        <h2>Core Values</h2>
        <ul>
          <li>• We believe camp ministry to be a highly effective way to minister to young people.</li>
          <li>• We teach Biblical truth in love.</li>
          <li>• We provide leadership and ministry opportunities for our counselors and staff members.</li>
          <li>• We believe that the summer camp experience provides opportunities for creating and strengthening lifelong Christ-centered relationships.</li>
          <li>• We believe that the glory of God can be seen and experienced through His creation in nature.</li>
          <li>• We believe it is important to bring glory to God by being good stewards of the gifts given to the mission of Camp Thornbrook.</li>
          <li>• We want to provide the best experience possible for a reasonable price.</li>
        </ul>
      </article>
    </section>
  </main>
</body>
</html>
```